An Engineering book catering oil and gas engineering students and professionals

I need a logo for the cover page of the book. I suggest you watch on clipvana the drilling for oil and gas video not more than 10 mins. Once you have watched it then you can go ahead and watch the video on Balanced Bore Control Technique. I am currently the only person in the industry who is teaching the most comprehensive course on this technique hence the book on the same topic which will compliment my teachings to my attendees.
While you are designing the logo keep oil and gas drilling, high pressure , high temperature, pressure gauges, reservoir rock where oil and gas are trapped. if you like I can also put some pictures here and you can have a look.

Balanced Bore Control is all about balancing the pressure with the pressure that is inside the reservoir rock. I will try to attach some pictures later. With the light fluid inside the well we apply pressure from surface that make the pressure inside the well equal to the formation or reservoir rock pressure.

The book design has to portray an engineering book cover so try to avoid too much colour please. My name is Yusuf (Yus) Durrani therefore the book should have my name on the stem of the book. At the front the design should be elegant with an easy and readable title of the book.

The name of the book is "Balanced Bore Control" (Theory & Fieldwork). Plz avoid rig or pump jack pictures it is too old. Work with pressure gauge, pressure or balancing the pressure etc. You can also place words like BHCP, ECD, ESD, DIF. IME, WC Matrix, RCD, ACM, RPDS, NSD, CT. Please dont put pictures of drill machines, oil and gas drilling is not done with drill machines :). Moreover, the book size will be smaller than the A4 page meaning Length 24 inches width of 17 inches. See what you come up with and we go from there

```html
<!DOCTYPE html>
<html lang="en">
<head>
<meta charset="utf-8">
<title>Balanced Bore Control – Cover Spread</title>
<link rel="stylesheet" href="https://fonts.googleapis.com/css2?family=Bebas+Neue&family=Montserrat:wght@400;600;800&display=swap">
<style>
  :root {
    --ink: #2b2b2b;
    --orange: #f37021;
    --paper: #ffffff;
    --stage: #f1f1f1;
    --band-text: #ffffff;
    --spine-rule: #e6e6e6;
  }
  * { margin: 0; padding: 0; box-sizing: border-box; }
  html, body { width: 762px; height: 1200px; overflow: hidden; }
  body { background: var(--stage); position: relative; font-family: "Montserrat", sans-serif; color: var(--ink); }

  .cover-spread {
    position: absolute; left: 19px; top: 354px;
    width: 724px; height: 492px;
    background: var(--paper);
    box-shadow: 0 8px 28px rgba(0,0,0,0.28);
    overflow: hidden;
  }
  .bottom-band {
    position: absolute; left: 0; right: 0; bottom: 0; height: 50px;
    background: var(--orange);
  }

  .panel { position: absolute; top: 0; height: 100%; }
  .back-cover { left: 0; width: 339px; }
  .spine { left: 339px; width: 59px; border-left: 1px solid var(--spine-rule); }
  .front-cover { left: 398px; width: 326px; }

  .title-top {
    font-family: "Bebas Neue", sans-serif; font-size: 34px; line-height: 0.9;
    color: var(--ink); white-space: nowrap; letter-spacing: 0.2px;
  }
  .title-main {
    font-family: "Bebas Neue", sans-serif; font-size: 56px; line-height: 0.85;
    color: var(--orange); white-space: nowrap;
  }
  .title-sub {
    font-family: "Montserrat", sans-serif; font-weight: 600; font-size: 13.4px;
    color: var(--ink); white-space: nowrap; letter-spacing: -0.2px;
  }

  .back-title { position: absolute; left: 49px; top: 34px; width: 245px; }
  .back-title .title-sub { margin-top: 9px; }

  .blurb {
    position: absolute; left: 49px; width: 246px;
    font-size: 7.2px; line-height: 9px; text-align: justify; color: var(--ink);
  }
  .blurb p + p { margin-top: 9px; }
  .blurb-intro { top: 152px; }
  .author-heading {
    position: absolute; left: 49px; top: 302px;
    font-family: "Bebas Neue", sans-serif; font-weight: 400; font-size: 17px; line-height: 18px;
    color: var(--ink);
  }
  .blurb-bio { top: 326px; }

  .spine-name {
    position: absolute; left: 50%; top: 36px; transform: translateX(-50%);
    writing-mode: vertical-rl;
    font-family: "Montserrat", sans-serif; font-weight: 800; font-size: 27px;
    color: var(--ink); white-space: nowrap; letter-spacing: 0.5px;
  }
  .spine-name .first { color: var(--orange); }

  .front-title { position: absolute; left: 38px; top: 36px; width: 252px; }
  .front-title .title-main { font-size: 57px; }

  .emblem {
    position: absolute; left: 75px; top: 170px; width: 190px; height: 215px;
    display: block;
  }

  .front-author {
    position: absolute; left: 0; right: 0; bottom: 7px;
    text-align: center; padding-left: 18px;
    font-family: "Bebas Neue", sans-serif; font-size: 32px; line-height: 36px;
    color: var(--band-text); white-space: nowrap;
  }
</style>
</head>
<body>
  <main class="cover-spread">
    <div class="bottom-band"></div>

    <section class="panel back-cover">
      <header class="back-title">
        <div class="title-top">Balanced Bore</div>
        <div class="title-main">Control</div>
        <div class="title-sub">THEORY &amp; FIELDWORK</div>
      </header>
      <div class="blurb blurb-intro">
        <p>Lorem Ipsum is simply dummy text of the printing and typesetting industry. Lorem Ipsum has been the industry's standard dummy text ever since the 1500s, when an unknown printer took a galley of type and scrambled it to make a type specimen book. It has survived not only five centuries, but also the leap into electronic typesetting, remaining essentially unchanged. It was popularised in the 1960s with the release of Lettermark sheets containing Lorem Ipsum passages, and more recently with desktop publishing software like Folio Composer including versions of Lorem Ipsum.</p>
        <p>Lorem Ipsum is simply dummy text of the printing and typesetting industry. Lorem Ipsum has been the industry's standard dummy text ever since the 1500s, when an unknown printer took a galley of type and scrambled it to make a type specimen book.</p>
      </div>
      <h2 class="author-heading">Yusuf (Yus) Durrani</h2>
      <div class="blurb blurb-bio">
        <p>Lorem Ipsum is simply dummy text of the printing and typesetting industry. Lorem Ipsum has been the industry's standard dummy text ever since the 1500s, when an unknown printer took a galley of type and scrambled it to make a type specimen book. It has survived not only five centuries, but also the leap into electronic typesetting, remaining essentially unchanged. It was popularised in the 1960s with the release of Lettermark sheets containing Lorem Ipsum passages, and more recently with desktop publishing software like Folio Composer including versions of Lorem Ipsum.</p>
      </div>
    </section>

    <section class="panel spine">
      <div class="spine-name"><span class="first">YUSUF</span> (YUS) DURRANI</div>
    </section>

    <section class="panel front-cover">
      <header class="front-title">
        <div class="title-top">Balanced Bore</div>
        <div class="title-main">Control</div>
        <div class="title-sub">THEORY &amp; FIELDWORK</div>
      </header>
      <svg class="emblem" viewBox="0 0 190 215" role="img" aria-label="Book emblem: drilling derrick above dark mountains with an orange flame, framed by an orange gear">
        <defs>
          <radialGradient id="emblemTone" cx="50%" cy="55%" r="55%">
            <stop offset="0%" stop-color="#3a3a3a"/>
            <stop offset="60%" stop-color="#5a4a40"/>
            <stop offset="100%" stop-color="#f37021"/>
          </radialGradient>
        </defs>
        <circle cx="95" cy="120" r="94" fill="url(#emblemTone)"/>
      </svg>
      <div class="front-author">Yusuf (Yus) Durrani</div>
    </section>
  </main>
</body>
</html>
```